Brenwick Shield Bundle: Two-Sided laminate to promote our paint, wheel and tire coverage products.

This is a redesign of the example document (Brenwick Shield Bundle Laminate.pdf) for our vehicle protection product package. This will contain the information given in the example on a two-sided document. Colors, fonts, and theme must align with the brand guidelines provided.

Target Market(s)

Middle-class pre-owned vehicle buyers

Industry/Entity Type

Automotive

Font styles to use
Other font styles liked:
• Poppins, Bebas Neue

Requirements
Must have
• Adhere to the color and look of our brand guidelines.
Nice to have
• Good visuals and icons to represent the products in the package.
Should not have
• No cartoon or animated graphics.

```html
<!DOCTYPE html>
<html lang="en">
<head>
<meta charset="utf-8">
<title>Brenwick Shield Bundle – Laminate</title>
<link href="https://fonts.googleapis.com/css2?family=Archivo+Black&family=Poppins:wght@500;600;700&display=swap" rel="stylesheet">
<style>
:root{
  --yellow:#fec425;
  --black:#0b0b0b;
  --white:#ffffff;
  --stage:#7d7d7d;
  --head:"Archivo Black", "Arial Black", sans-serif;
  --body:"Poppins", Arial, sans-serif;
}
*{box-sizing:border-box;margin:0;padding:0}
html,body{width:889px;height:1200px;overflow:hidden}
body{background:var(--stage);position:relative;font-family:var(--body);color:var(--black)}
.sheet{position:absolute;top:300px;width:420px;height:600px;overflow:hidden;box-shadow:0 10px 24px rgba(0,0,0,.45)}
.sheet--benefits{left:12px;background:var(--white)}
.sheet--bundle{left:457px;background:var(--yellow)}

/* Benefits side */
.benefits__top{position:absolute;left:0;top:0;width:100%;height:242px;background:var(--black)}
.brand{position:absolute;left:70px;top:24px;width:280px;height:62px;background:#1d1d1d;border-radius:3px;padding:6px 8px;text-align:center}
.brand__name{display:block;background:var(--white);color:var(--black);font-family:var(--head);font-size:22px;line-height:32px;letter-spacing:.5px}
.brand__place{display:block;color:var(--yellow);font-family:var(--head);font-size:9px;letter-spacing:6px;margin-top:4px}
.benefits__title{position:absolute;top:100px;width:100%;text-align:center;color:var(--white);font-family:var(--head);font-size:26px;letter-spacing:.5px}
.pill{position:absolute;top:146px;width:122px;height:324px;background:var(--yellow);border-radius:61px;padding:0 10px}
.pill--paint{left:19px}.pill--wheel{left:149px}.pill--tire{left:279px}
.pill__icon{display:block;margin:10px auto 0;width:100px;height:100px;border-radius:50%;background:radial-gradient(circle at 50% 45%,#555 0%,#1c1c1c 60%,#000 100%)}
.pill__title{font-family:var(--head);font-size:14px;line-height:14px;text-align:center;margin-top:6px}
.pill__list{list-style:none;margin-top:8px;font-size:5.6px;line-height:6.6px;font-weight:600}
.pill__list li{position:relative;padding-left:11px;margin-bottom:7px}
.pill__list li::before{content:"";position:absolute;left:1px;top:1px;width:5px;height:5px;border:1px solid var(--black);border-radius:1px}
.pill__sub{list-style:none;margin:5px 0 0 6px}
.pill__sub li{padding-left:7px;margin-bottom:1.5px}
.pill__sub li::before{border:none;border-left:1px solid var(--black);border-bottom:1px solid var(--black);width:4px;height:2px;transform:rotate(-45deg);top:2px}
.faq{position:absolute;left:18px;top:484px;width:214px}
.faq__title{font-family:var(--head);font-size:22px;line-height:22px}
.faq__q{font-size:8px;line-height:9px;font-weight:700;margin-top:3px}
.faq__a{font-size:5.4px;line-height:7px;font-weight:600;margin-top:6px}
.photo{position:absolute}
.photo--truck{left:238px;top:474px;width:180px;height:92px;border-radius:14px 20px 10px 10px;background:linear-gradient(160deg,#d4d4d4 0%,#9a9a9a 55%,#3a3a3a 100%)}

/* Footer */
.footer{position:absolute;left:0;bottom:0;width:100%;height:32px;background:var(--yellow);display:flex;align-items:center;font-weight:700}
.footer__phone{width:170px;padding-left:16px;display:flex;align-items:center;gap:5px;font-size:11px;border-right:1.5px solid var(--black);height:20px}
.footer__addr{flex:1;display:flex;align-items:center;justify-content:center;gap:5px;font-size:7px}

/* Bundle side */
.bundle__white{position:absolute;left:0;top:241px;width:100%;height:327px;background:var(--white)}
.bundle__title{position:absolute;top:20px;width:100%;text-align:center;font-family:var(--head);font-size:30px;line-height:36px;letter-spacing:.3px}
.panel{position:absolute;left:18px;top:63px;width:384px;height:420px;background:var(--black);border-radius:30px;padding:20px 22px 0 22px;color:var(--yellow)}
.row{position:relative;border-bottom:1px solid rgba(254,196,37,.45);padding-right:110px}
.row--paint{height:90px}.row--wheel{height:62px;padding-top:8px}.row--tire{height:75px;padding-top:8px}.row--nitro{height:54px;padding-top:8px;border:none}
.row__name{font-family:var(--head);font-size:15px;line-height:18px}
.row__price{position:absolute;right:0;top:50%;transform:translateY(-50%);font-family:var(--head);font-size:27px;line-height:30px}
.row__list{list-style:none;font-size:6px;line-height:10px;font-weight:600}
.row__list li{position:relative;padding-left:9px;white-space:nowrap}
.row__list li::before{content:"";position:absolute;left:0;top:3px;width:4px;height:4px;border:.8px solid var(--yellow)}
.row__dots{display:grid;grid-template-columns:repeat(3,60px);margin:5px 0 5px 14px;font-size:5.6px;line-height:8px;font-weight:600}
.row__dots span::before{content:"• "}
.total{text-align:center;margin-top:2px}
.total__amount{display:block;color:var(--white);font-family:var(--head);font-size:34px;line-height:36px}
.total__label{display:block;font-family:var(--head);font-size:22px;line-height:22px}
.photo--sedan{left:98px;top:458px;width:212px;height:108px;border-radius:50px 70px 14px 14px;background:linear-gradient(170deg,#4a4f57 0%,#1b1d21 55%,#050505 100%)}
</style>
</head>
<body>

<section class="sheet sheet--benefits" aria-label="Benefits side">
  <div class="benefits__top"></div>
  <div class="brand">
    <span class="brand__name">BRENWICK CARS</span>
    <span class="brand__place">HARLOW FALLS</span>
  </div>
  <h1 class="benefits__title">BENEFITS</h1>

  <article class="pill pill--paint">
    <svg class="pill__icon" viewBox="0 0 100 100" fill="none" stroke="#fff" stroke-width="2.4" stroke-linecap="round" stroke-linejoin="round">
      <path d="M50 26 L64 31 V43 C64 52 58 58 50 61 C42 58 36 52 36 43 V31 Z"/>
      <path d="M44 43 L49 48 L57 38"/>
      <path d="M30 48 V64 L42 76 M70 48 V64 L58 76"/>
    </svg>
    <h2 class="pill__title">Luster Paint Protection</h2>
    <ul class="pill__list">
      <li>LUSTER paint coating protects from the following damages:
        <ul class="pill__sub">
          <li>Bird Droppings</li><li>Sun Damage</li><li>Hard Water</li>
          <li>Insect Damage</li><li>Road Salt</li><li>Oxidation</li>
        </ul>
      </li>
      <li>LUSTER paint coating protects from the following damages:</li>
    </ul>
  </article>

  <article class="pill pill--wheel">
    <svg class="pill__icon" viewBox="0 0 100 100" fill="none" stroke="#fff" stroke-width="2.4" stroke-linecap="round" stroke-linejoin="round">
      <circle cx="50" cy="44" r="17"/><circle cx="50" cy="44" r="12"/>
      <path d="M50 37 L52 42 L57 42 L53 45 L55 50 L50 47 L45 50 L47 45 L43 42 L48 42 Z"/>
      <path d="M40 58 L35 72 L41 70 L44 75 L48 61 M60 58 L65 72 L59 70 L56 75 L52 61"/>
    </svg>
    <h2 class="pill__title">Wheel/Rim Warranty</h2>
    <ul class="pill__list">
      <li>4 replacement rims per contract at $400 per rim</li>
      <li>Damage must be a breakdown or failure of the rim/rim must not be able to hold air or function</li>
      <li>Does not cover scratches or imperfections which do not qualify as a breakdown</li>
      <li>Does not include environmental damage such as corrosion</li>
    </ul>
  </article>

  <article class="pill pill--tire">
    <svg class="pill__icon" viewBox="0 0 100 100" fill="none" stroke="#fff" stroke-width="2.4" stroke-linecap="round" stroke-linejoin="round">
      <circle cx="50" cy="38" r="11"/>
      <path d="M50 33 L51.5 36.5 L55 36.5 L52 39 L53 42.5 L50 40.5 L47 42.5 L48 39 L45 36.5 L48.5 36.5 Z"/>
      <path d="M28 44 V60 L40 72 H46 V62 L38 54 M72 44 V60 L60 72 H54 V62 L62 54"/>
    </svg>
    <h2 class="pill__title">Nitrogen Tire Benefit</h2>
    <ul class="pill__list">
      <li>4 replacement tires per contract at $200 per tire</li>
      <li>Tire must be damaged from road hazard</li>
      <li>4 replacement tires per contract (regardless of number of years on contract) Unlimited flat tire repairs at Brenwick</li>
      <li>Flats must be caused by road hazard while tread depth is above 3/32 inch. Nitrogen tire inflation</li>
      <li>Free nitrogen refill when tires are low or have been filled with air</li>
    </ul>
  </article>

  <div class="faq">
    <h2 class="faq__title">FAQS</h2>
    <p class="faq__q">Can I mix air with Nitrogen if I have a flat, or need to add air pressure?</p>
    <p class="faq__a">Yes, tire can be inflated with air until tire/rim is repaired. Tire must be filled with Nitrogen after repair for contract to be valid.</p>
  </div>
  <div class="photo photo--truck" role="img" aria-label="Photo of a silver full-size pickup truck"></div>

  <footer class="footer">
    <div class="footer__phone">
      <svg width="11" height="11" viewBox="0 0 24 24" fill="#0b0b0b"><path d="M6.6 10.8a15 15 0 0 0 6.6 6.6l2.2-2.2c.3-.3.7-.4 1-.2 1.1.4 2.3.6 3.6.6.6 0 1 .4 1 1V20c0 .6-.4 1-1 1A17 17 0 0 1 3 4c0-.6.4-1 1-1h3.5c.6 0 1 .4 1 1 0 1.3.2 2.5.6 3.6.1.3 0 .7-.2 1z"/></svg>
      <span>SALES (555) 014-2000</span>
    </div>
    <div class="footer__addr">
      <svg width="8" height="10" viewBox="0 0 24 30" fill="none" stroke="#0b0b0b" stroke-width="3"><path d="M12 28s9-9 9-16a9 9 0 0 0-18 0c0 7 9 16 9 16z"/><circle cx="12" cy="12" r="3.5"/></svg>
      <span>418 ALDER AVE HARLOW FALLS NE 68000</span>
    </div>
  </footer>
</section>

<section class="sheet sheet--bundle" aria-label="Shield Bundle side">
  <div class="bundle__white"></div>
  <h1 class="bundle__title">SHIELD BUNDLE</h1>

  <div class="panel">
    <div class="row row--paint">
      <h2 class="row__name">Luster Paint Protection</h2>
      <ul class="row__list"><li>LUSTER paint coating protects from the following damages:</li></ul>
      <div class="row__dots">
        <span>Bird Droppings</span><span>Hard Water</span><span>Road Salt</span>
        <span>Sun Damage</span><span>Insect Damage</span><span>Oxidation</span>
      </div>
      <ul class="row__list"><li>Warranty provides paint repair for the items listed above</li></ul>
      <span class="row__price">$2,500</span>
    </div>
    <div class="row row--wheel">
      <h2 class="row__name">Wheel /Rim Warranty</h2>
      <ul class="row__list"><li>Replacement for potholes/road hazard</li><li>$400 per wheel/4 wheels per contract</li></ul>
      <span class="row__price">$1,600</span>
    </div>
    <div class="row row--tire">
      <h2 class="row__name">Tire Warranty</h2>
      <ul class="row__list"><li>Replacement for potholes/road hazard</li><li>$200 per tire/4 tires per contract</li><li>Unlimited flat tire repair</li></ul>
      <span class="row__price">$800</span>
    </div>
    <div class="row row--nitro">
      <h2 class="row__name">Nitrogen Tire Inflation</h2>
      <ul class="row__list"><li>Free Nitrogen refills at Brenwick</li></ul>
      <span class="row__price">$50</span>
    </div>
    <p class="total">
      <span class="total__amount">$4,950</span>
      <span class="total__label">Potential Warranty<br>Value</span>
    </p>
  </div>
  <div class="photo photo--sedan" role="img" aria-label="Photo of a black sport sedan"></div>

  <footer class="footer">
    <div class="footer__phone">
      <svg width="11" height="11" viewBox="0 0 24 24" fill="#0b0b0b"><path d="M6.6 10.8a15 15 0 0 0 6.6 6.6l2.2-2.2c.3-.3.7-.4 1-.2 1.1.4 2.3.6 3.6.6.6 0 1 .4 1 1V20c0 .6-.4 1-1 1A17 17 0 0 1 3 4c0-.6.4-1 1-1h3.5c.6 0 1 .4 1 1 0 1.3.2 2.5.6 3.6.1.3 0 .7-.2 1z"/></svg>
      <span>SALES (555) 014-2000</span>
    </div>
    <div class="footer__addr">
      <svg width="8" height="10" viewBox="0 0 24 30" fill="none" stroke="#0b0b0b" stroke-width="3"><path d="M12 28s9-9 9-16a9 9 0 0 0-18 0c0 7 9 16 9 16z"/><circle cx="12" cy="12" r="3.5"/></svg>
      <span>418 ALDER AVE HARLOW FALLS NE 68000</span>
    </div>
  </footer>
</section>

</body>
</html>
```